Design for sports training app

We need the design for 9 screens of an app that supports trainers of sport teams in preparing their training sessions. Regarding colors, fonts etc. there is absolute freedom for the designer to choose what he thinks is best.
The app will be called "Vellix", our idea for the logo is something like a stopwatch.
Wireframes are attached for every screen. You don't have to stick to those - if you have better ideas, we are happy to see them.
Our strategy is "mobile first". Based on the app design we will create a homepage later - I guess it makes sense to give this to the same person, let's see.
The deliverables are attached.
All in all the main target is to present a very simple, intuitive and nice UI that the user can work with without much learning.
Updates
Target Market(s)
Soccer trainers
Industry/Entity Type
Training
Look and feel

```html
<!DOCTYPE html>
<html lang="en">
<head>
<meta charset="utf-8">
<title>Offensive 2 vs. 1 – Skill Focus</title>
<link rel="stylesheet" href="https://fonts.googleapis.com/css2?family=Source+Sans+3:wght@300;400&display=swap">
<style>
  :root {
    --backdrop: #33363c;
    --brand-blue: #5580f7;
    --brand-blue-light: #6a90f8;
    --surface: #ffffff;
    --track: #e3e3e6;
    --label: #4a4a4f;
    --on-brand: #ffffff;
    --coordination: #3dbbd6;
    --finishing: #7b49f5;
    --stamina: #8fa2ad;
    --speed: #4fae4a;
    --understanding: #86c23e;
    --defensive: #f1c232;
  }
  * { box-sizing: border-box; margin: 0; padding: 0; }
  html, body {
    width: 1200px; height: 900px; overflow: hidden;
    background: var(--backdrop);
    font-family: "Source Sans 3", "Helvetica Neue", Arial, sans-serif;
  }
  .stage {
    width: 1200px; height: 900px;
    display: flex; align-items: center; justify-content: center;
  }
  .app-screen {
    width: 450px; height: 800px;
    background: var(--surface);
    display: flex; flex-direction: column;
    box-shadow: 0 20px 50px rgba(0,0,0,.35);
  }
  .app-header {
    background: var(--brand-blue);
    color: var(--on-brand);
    padding: 0 18px 18px;
  }
  .status-bar {
    height: 30px;
    display: flex; align-items: center; justify-content: space-between;
    font-size: 14px; font-weight: 400;
  }
  .status-left { display: flex; align-items: center; gap: 8px; }
  .signal { display: flex; gap: 3px; }
  .signal span { width: 7px; height: 7px; border-radius: 50%; background: var(--on-brand); }
  .signal span.empty { background: transparent; border: 1px solid var(--on-brand); }
  .nav-bar {
    position: relative; height: 44px;
    display: flex; align-items: center; justify-content: center;
  }
  .nav-back { position: absolute; left: 0; top: 50%; transform: translateY(-50%); }
  .nav-title { font-size: 24px; font-weight: 300; letter-spacing: .2px; }

  .skill-list {
    flex: 1; list-style: none;
    padding: 40px 34px 0;
    display: flex; flex-direction: column; gap: 30px;
  }
  .skill-name {
    font-size: 17px; font-weight: 300; color: var(--label);
    margin-bottom: 10px;
  }
  .skill-track {
    height: 10px; border-radius: 5px; background: var(--track);
    overflow: hidden;
  }
  .skill-fill { height: 100%; border-radius: 5px; }
  .skill-coordination .skill-fill { width: 62%; background: var(--coordination); }
  .skill-finishing .skill-fill { width: 36%; background: var(--finishing); }
  .skill-stamina .skill-fill { width: 56%; background: var(--stamina); }
  .skill-speed .skill-fill { width: 19%; background: var(--speed); }
  .skill-understanding .skill-fill { width: 37%; background: var(--understanding); }
  .skill-defensive .skill-fill { width: 36%; background: var(--defensive); }

  .tab-bar {
    height: 84px; background: var(--brand-blue);
    display: flex; align-items: center; justify-content: space-around;
  }
  .tab-bar svg { display: block; }
</style>
</head>
<body>
<main class="stage">
  <section class="app-screen">
    <header class="app-header">
      <div class="status-bar">
        <div class="status-left">
          <div class="signal"><span></span><span></span><span></span><span></span><span class="empty"></span></div>
          <svg width="16" height="12" viewBox="0 0 16 12" fill="none" stroke="#fff" stroke-width="1.6" stroke-linecap="round">
            <path d="M1 4.5a10 10 0 0 1 14 0"/><path d="M3.5 7a6.5 6.5 0 0 1 9 0"/><circle cx="8" cy="10" r="1" fill="#fff"/>
          </svg>
        </div>
        <span class="status-time">4:21 PM</span>
        <svg width="28" height="12" viewBox="0 0 28 12">
          <rect x="0.5" y="0.5" width="24" height="11" rx="2" fill="none" stroke="#fff"/>
          <rect x="2" y="2" width="21" height="8" rx="1" fill="#fff"/>
          <rect x="25.5" y="4" width="2" height="4" rx="1" fill="#fff"/>
        </svg>
      </div>
      <div class="nav-bar">
        <svg class="nav-back" width="14" height="22" viewBox="0 0 14 22" fill="none" stroke="#fff" stroke-width="1.8" stroke-linecap="round" stroke-linejoin="round">
          <path d="M12 2 2 11l10 9"/>
        </svg>
        <h1 class="nav-title">Offensive 2 vs. 1</h1>
      </div>
    </header>

    <ul class="skill-list">
      <li class="skill skill-coordination"><p class="skill-name">Coordination</p><div class="skill-track"><div class="skill-fill"></div></div></li>
      <li class="skill skill-finishing"><p class="skill-name">Finishing</p><div class="skill-track"><div class="skill-fill"></div></div></li>
      <li class="skill skill-stamina"><p class="skill-name">Stamina</p><div class="skill-track"><div class="skill-fill"></div></div></li>
      <li class="skill skill-speed"><p class="skill-name">Speed</p><div class="skill-track"><div class="skill-fill"></div></div></li>
      <li class="skill skill-understanding"><p class="skill-name">Understanding of the game</p><div class="skill-track"><div class="skill-fill"></div></div></li>
      <li class="skill skill-defensive"><p class="skill-name">Devensive behaviour</p><div class="skill-track"><div class="skill-fill"></div></div></li>
    </ul>

    <nav class="tab-bar">
      <svg class="tab-info" width="34" height="34" viewBox="0 0 34 34" fill="none" stroke="#fff" stroke-width="2.2" stroke-linecap="round">
        <circle cx="17" cy="17" r="14"/>
        <circle cx="17.5" cy="10.5" r="1.2" fill="#fff" stroke="none"/>
        <path d="M17 15v9"/>
      </svg>
      <svg class="tab-skills" width="40" height="34" viewBox="0 0 40 34" fill="#fff" stroke="#fff" stroke-width="3" stroke-linecap="round">
        <circle cx="6" cy="8" r="2.4" stroke="none"/><circle cx="15" cy="5" r="2.4" stroke="none"/>
        <circle cx="24" cy="4" r="2.4" stroke="none"/><circle cx="33" cy="6" r="2.4" stroke="none"/>
        <path d="M6 15v14"/><path d="M15 13v16"/><path d="M24 12v17"/><path d="M33 14v15"/>
      </svg>
      <svg class="tab-search" width="32" height="36" viewBox="0 0 32 36" fill="none" stroke="#fff" stroke-width="3" stroke-linecap="round">
        <circle cx="16" cy="13" r="10"/><path d="M16 23v11"/>
      </svg>
    </nav>
  </section>
</main>
</body>
</html>
```